Luxury Bath Flyer

I would like to have a professional Flyer, which would describe a beautiful atmospheric luxury-Bath situation. I am sending you a( screenshot) Flyer Proposal, which shoes my intention and wish how I would like to have it. Please note that Ästhetik and a professional Flyer is very important to me. If possible send a psd.file or a indesign file, in case of we gonna need to change the text. You are also free to make 2 different proposals and one as you would suggest.?(I send you couple pictures, but the main one which I choose on the pdf file, please keep that, it is called " KR-71" - If there is a question please let me know. Looking forward to receive an amazing artwork.Kind Regards Merle
Look and feel
Each slider illustrates characteristics of the customer's brand and the style your logo design should communicate.

```html
<!DOCTYPE html>
<html lang="en">
<head>
<meta charset="utf-8">
<title>Luxury Bath Flyer</title>
<link href="https://fonts.googleapis.com/css2?family=Source+Sans+3:wght@400;700&display=swap" rel="stylesheet">
<style>
  :root {
    --backdrop: #e9eaec;
    --navy: #0a4b8c;
    --sky: #2fb1e5;
    --ink: #1f1f1f;
    --paper: #ffffff;
    --photo-light: #d9d2c8;
    --photo-mid: #a89482;
    --photo-dark: #5c4a3c;
  }
  * { box-sizing: border-box; margin: 0; padding: 0; }
  html, body {
    width: 1200px; height: 1200px; overflow: hidden;
    background: var(--backdrop);
    font-family: "Source Sans 3", "Myriad Pro", sans-serif;
  }
  .flyer-frame {
    position: absolute; left: 207px; top: 50px;
    width: 785px; height: 1100px;
  }
  .flyer {
    position: absolute; left: 0; top: 0;
    width: 850px; height: 1191px;
    background: var(--paper);
    transform: scale(0.9236); transform-origin: 0 0;
    overflow: hidden;
  }
  .flyer-shapes { position: absolute; inset: 0; width: 850px; height: 1191px; }
  .logo {
    position: absolute; left: 596px; top: 86px;
    font-size: 66px; font-weight: 700; color: var(--navy);
    letter-spacing: -1px;
  }
  .headline {
    position: absolute; left: 106px; top: 724px;
    font-size: 46px; font-weight: 700; line-height: 47px;
    color: var(--navy); white-space: nowrap; letter-spacing: -0.3px;
  }
  .headline-rule {
    position: absolute; left: 103px; top: 830px;
    width: 672px; height: 5px; border-radius: 3px; background: var(--sky);
  }
  .body-copy {
    position: absolute; left: 49px; top: 855px; width: 770px;
    font-size: 18.2px; line-height: 23.4px; color: var(--ink);
    white-space: nowrap;
  }
  .body-copy p + p { margin-top: 11px; }
  .contact-call {
    position: absolute; left: 0; top: 1062px; width: 850px; height: 56px;
    background: var(--sky); color: var(--paper);
    font-size: 33px; line-height: 56px; text-align: center;
  }
  .contact-details {
    position: absolute; left: 0; top: 1118px; width: 850px; height: 73px;
    background: var(--navy); color: var(--paper);
    font-size: 20px; line-height: 54px; text-align: center;
    word-spacing: 2px;
  }
  .contact-details .sep { margin: 0 16px; }
</style>
</head>
<body>
  <div class="flyer-frame">
    <div class="flyer">
      <svg class="flyer-shapes" viewBox="0 0 850 1191" aria-hidden="false">
        <defs>
          <linearGradient id="roomTones" x1="0" y1="0" x2="0.3" y2="1">
            <stop offset="0" stop-color="var(--photo-light)"/>
            <stop offset="0.55" stop-color="var(--photo-mid)"/>
            <stop offset="1" stop-color="var(--photo-dark)"/>
          </linearGradient>
          <linearGradient id="basinTones" x1="0" y1="0" x2="0" y2="1">
            <stop offset="0" stop-color="#c9a98b"/>
            <stop offset="0.6" stop-color="#e6ddd3"/>
            <stop offset="1" stop-color="#f4f1ec"/>
          </linearGradient>
        </defs>
        <path class="wave-band" fill="var(--navy)"
              d="M0,540 H850 V634 C780,648 680,664 580,662 C380,660 180,620 0,578 Z"/>
        <path class="hero-photo" fill="url(#roomTones)" role="img"
              aria-label="Photo of a luxury bathroom with wooden vanity, tall cabinet and freestanding bathtub"
              d="M0,0 H850 V591 C790,604 690,626 578,626 C400,626 200,590 0,552 Z"/>
        <circle class="detail-photo" cx="175" cy="574" r="139" fill="url(#basinTones)"
                stroke="var(--sky)" stroke-width="8" role="img"
                aria-label="Close-up photo of a white basin with chrome taps and mosaic tiles"/>
      </svg>

      <div class="logo">LOGO</div>

      <h1 class="headline">LOREM IPSUM DOLOR SIT AMET<br>CONSECTETUR ADIPISCING ELIT</h1>
      <div class="headline-rule"></div>

      <div class="body-copy">
        <p>Lorem ipsum dolor sit amet, consectetur adipiscing elit, sed do eiusmod tempor incididunt ut<br>
        labore et dolore magna aliqua. Ut enim ad minim veniam, quis nostrud exercitation ullamco<br>
        laboris nisi ut aliquip ex ea commodo consequat. Duis aute irure dolor in reprehenderit in<br>
        voluptate velit esse cillum dolore eu fugiat nulla pariatur. Excepteur sint occaecat cupidatat<br>
        non proident, sunt in culpa qui officia deserunt mollit anim id est laborum.</p>
        <p>Lorem ipsum dolor sit amet, consectetur adipiscing elit, sed do eiusmod tempor incididunt ut<br>
        labore et dolore magna aliqua. Ut enim ad minim veniam, quis nostrud exercitation ullamco la</p>
      </div>

      <div class="contact-call">For More Details &amp; Informatin Please Contact Us</div>
      <div class="contact-details">
        0987654321<span class="sep">|</span>hello@bathstudio.com<span class="sep">|</span>www.bathstudio.com
      </div>
    </div>
  </div>
</body>
</html>
```